New Business Card Design Project

I have a logo I would like to use on the business card. I want something that will stand out and that will be remembered.

Target Market(s)

People who collect gems, minerals and crystals.

Contact Information for Business Card

email - tkstonefalcon@mailbrook.net
phone # 617-203-4958

Font styles to use
Serif
Sans Serif
Decorative

Colors

Designer to choose colors to be used in the design.

Requirements
Must have
• The logo...two to choose from.
Nice to have
• An eye catching and memorable way to draw in people who collect gems minerals and crystals.

```html
<!DOCTYPE html>
<html lang="en">
<head>
<meta charset="utf-8">
<title>Stone Falcon – Business Card</title>
<link rel="stylesheet" href="https://fonts.googleapis.com/css2?family=Saira:wght@400;600&display=swap">
<style>
  :root {
    --page-bg: #eceae8;
    --card-edge: #1c1c1c;
    --card-centre: #4a4a4a;
    --card-dark: #161616;
    --ink-light: #f2f2f2;
    --ink-silver: #c9c9c9;
  }
  * { margin: 0; padding: 0; box-sizing: border-box; }
  html, body {
    width: 1200px;
    height: 900px;
    overflow: hidden;
    background: var(--page-bg);
  }
  .canvas {
    position: relative;
    width: 1200px;
    height: 900px;
  }
  .business-card {
    position: absolute;
    left: 100px;
    top: 165px;
    width: 1000px;
    height: 571px;
    background: radial-gradient(ellipse 70% 75% at 55% 40%, var(--card-centre) 0%, var(--card-edge) 70%, var(--card-dark) 100%);
    box-shadow: 0 12px 30px rgba(0, 0, 0, 0.25);
  }
  .brand {
    position: absolute;
    left: 60px;
    top: 45px;
    width: 300px;
    display: flex;
    flex-direction: column;
    align-items: center;
    gap: 22px;
  }
  .brand-mark {
    width: 130px;
    height: 130px;
    border-radius: 50%;
    background: var(--ink-silver);
  }
  .brand-name {
    font-family: "Saira", sans-serif;
    font-weight: 600;
    font-size: 54px;
    line-height: 1;
    letter-spacing: 3px;
    text-transform: uppercase;
    text-align: center;
    color: var(--ink-silver);
  }
  .contact {
    position: absolute;
    left: 540px;
    bottom: 60px;
    font-family: "Saira", sans-serif;
    font-style: normal;
    font-weight: 400;
    color: var(--ink-light);
    font-size: 26px;
    letter-spacing: 3px;
    line-height: 1.45;
  }
  .contact-phone,
  .contact-email { display: block; }
</style>
</head>
<body>
  <main class="canvas">
    <section class="business-card">
      <div class="brand">
        <span class="brand-mark" aria-hidden="true"></span>
        <span class="brand-name">Stone<br>Falcon</span>
      </div>
      <address class="contact">
        <span class="contact-phone">617 - 203 - 4958</span>
        <span class="contact-email">tkstonefalcon@mailbrook.net</span>
      </address>
    </section>
  </main>
</body>
</html>
```